Postcard for Geriatric Psychologists

Elmvale Associates is a practice of geriatric psychologists who provide counseling services in nursing homes. Our marketing is NOT directed toward senior citizens; it's directed toward nursing home administrators who have the authority to invite us into their facilities. We plan to mail postcards to about 100 administrators each month, meaning that we'll need 12 unique designs each year. The goal of this marketing strategy is to improve our name recognition in the professional community. Logo design is complete.

Target Market(s)

Nursing home administrators

Industry/Entity Type

Mental Health

Font styles to use
Serif

Requirements
Must have
• Our logo and a color scheme that matches it (see uploaded EPS file)
• Web address: Elmvale.net
• Phone: (555) 817-2093
Nice to have
• Image of happy senior citizens ... our patients are typically 80-100 years old
Should not have
• Images of brains or heads flipped open as if on a hinge

```html
<!DOCTYPE html>
<html lang="en">
<head>
<meta charset="utf-8">
<title>Elmvale Associates Postcard</title>
<link href="https://fonts.googleapis.com/css2?family=Montserrat:wght@400;500;600;700&display=swap" rel="stylesheet">
<style>
  :root {
    --page-bg: #e4e4e4;
    --card-bg: #f1f1f1;
    --brand-blue: #1a7fc1;
    --deep-blue: #2a55a6;
    --ink: #3a3a3a;
    --ink-dark: #222;
    --white: #ffffff;
    --stamp: #1a9ad8;
    --box-line: #b9bdc2;
  }
  * { box-sizing: border-box; margin: 0; padding: 0; }
  html, body { width: 960px; height: 1200px; overflow: hidden; }
  body {
    background: var(--page-bg);
    font-family: "Montserrat", sans-serif;
    position: relative;
  }
  .card {
    position: absolute;
    left: 138px;
    width: 677px;
    height: 524px;
    overflow: hidden;
    background: var(--card-bg);
  }
  .card--front { top: 54px; }
  .card--back { top: 618px; }

  /* Front */
  .brand {
    position: absolute;
    left: 18px; top: 40px;
    width: 200px;
    text-align: center;
    font-size: 16.5px;
    font-weight: 600;
    color: var(--ink-dark);
    line-height: 20px;
    white-space: nowrap;
  }
  .brand__mark {
    display: block;
    width: 46px; height: 46px;
    margin: 0 auto 14px;
    border-radius: 50%;
    background: var(--brand-blue);
  }
  .web-front {
    position: absolute;
    left: 38px; top: 162px;
    display: flex; align-items: center; gap: 6px;
    font-size: 17px; font-weight: 600; color: var(--ink-dark);
    white-space: nowrap;
  }
  .intro {
    position: absolute;
    left: 233px; top: 31px; width: 408px;
  }
  .intro__title { font-size: 12px; font-weight: 600; color: var(--brand-blue); margin-bottom: 6px; }
  .intro__body { font-size: 10.2px; line-height: 14px; color: var(--ink); }
  .intro__billing { font-size: 9.6px; font-weight: 600; color: var(--brand-blue); margin-top: 8px; }
  .callout {
    position: absolute;
    left: 233px; top: 136px; width: 403px;
    border-top: 2px solid var(--ink-dark);
    border-bottom: 2px solid var(--deep-blue);
    padding: 6px 0 7px;
    font-size: 15.6px; font-weight: 500; line-height: 20px;
    color: var(--brand-blue);
    white-space: nowrap;
  }
  .photo-seniors {
    position: absolute;
    left: 0; top: 230px; width: 677px; height: 294px;
    background: linear-gradient(180deg, #e6e4e2 0%, #cfc8c3 25%, #a9b7d3 60%, #7d8fc4 100%);
  }

  /* Back */
  .back-panel {
    position: absolute; left: 0; top: 0; width: 326px; height: 524px;
    background: linear-gradient(180deg, var(--deep-blue) 0%, #3a6db5 45%, #4a8ac6 75%, #3f7cb8 100%);
    color: var(--white);
  }
  .back-panel__headline {
    position: absolute; left: 29px; top: 31px; width: 276px;
    border-top: 2px solid var(--white); border-bottom: 2px solid var(--white);
    padding: 8px 0 7px;
    font-size: 16px; font-weight: 600; letter-spacing: 0.4px;
  }
  .back-panel__subhead {
    position: absolute; left: 0; top: 96px; width: 326px;
    text-align: center; font-size: 16px; font-weight: 600; letter-spacing: 0.3px;
  }
  .service {
    position: absolute; width: 145px;
    display: flex; align-items: center; gap: 6px;
  }
  .service--left { left: 29px; }
  .service--right { left: 181px; }
  .service__icon {
    flex: none; width: 51px; height: 51px; border-radius: 50%;
    background: var(--white);
    display: flex; align-items: center; justify-content: center;
  }
  .service__label { font-size: 11px; font-weight: 600; line-height: 14.5px; white-space: nowrap; }
  .contact {
    position: absolute; left: 0; top: 406px; width: 326px;
    text-align: center; font-size: 16px; font-weight: 600; line-height: 20px; letter-spacing: 0.4px;
  }
  .web-back {
    position: absolute; left: 0; top: 469px; width: 326px;
    display: flex; justify-content: center; align-items: center; gap: 6px;
    font-size: 17px; font-weight: 600;
  }
  .landscape {
    position: absolute; left: 326px; top: 0; width: 351px; height: 524px;
    background: linear-gradient(180deg, #f3f3f3 0%, #eceded 45%, #d2d5d8 70%, #c9cdd1 100%);
  }
  .stamp { position: absolute; left: 536px; top: 32px; }
  .address-line {
    position: absolute; left: 344px; width: 291px;
    border: 1.5px solid var(--box-line);
  }
  .address-line--top { top: 186px; height: 42px; }
  .address-line--main { top: 246px; height: 130px; }
</style>
</head>
<body>

<section class="card card--front">
  <div class="brand"><span class="brand__mark"></span>Elmvale Associates</div>
  <div class="web-front">
    <svg width="20" height="20" viewBox="0 0 20 20" fill="none" stroke="#222" stroke-width="1.4"><circle cx="10" cy="10" r="8.5"/><ellipse cx="10" cy="10" rx="3.8" ry="8.5"/><line x1="1.5" y1="10" x2="18.5" y2="10"/><line x1="3" y1="5.5" x2="17" y2="5.5"/><line x1="3" y1="14.5" x2="17" y2="14.5"/></svg>
    Elmvale.net
  </div>
  <div class="intro">
    <p class="intro__title">Elmvale Associates is a group practice in psychology.</p>
    <p class="intro__body">Our dedicated psychologists visit assisted living and nursing facilities each week to provide on-site counseling and evaluation services. We understand the value of teamwork, and we're happy to coordinate care with your staff. GIVE US A CALL TO LEARN MORE!</p>
    <p class="intro__billing">WE BILL INSURANCE DIRECTLY, SO THERE'S NO COST TO YOUR FACILITY!</p>
  </div>
  <p class="callout">CHECK OUT OUR WEBSITE TO SEE WHAT<br>YOUR COLLEAGUES ARE SAYING ABOUT US!</p>
  <div class="photo-seniors" role="img" aria-label="Photo of five smiling senior citizens standing together"></div>
</section>

<section class="card card--back">
  <div class="back-panel">
    <p class="back-panel__headline">NO COST TO YOUR FACILITY!</p>
    <p class="back-panel__subhead">Services We Provide</p>

    <div class="service service--left" style="top:150px;">
      <span class="service__icon"><svg width="28" height="28" viewBox="0 0 28 28"><path d="M14 3a9 9 0 0 0-9 9c0 3 1.4 5 3 6.5V25h10v-3h3l1-5 2-1-2-4A9 9 0 0 0 14 3z" fill="#2a55a6"/></svg></span>
      <span class="service__label">Psychological<br>Assessment &amp;<br>Diagnosis</span>
    </div>
    <div class="service service--right" style="top:150px;">
      <span class="service__icon"><svg width="28" height="28" viewBox="0 0 28 28"><path d="M14 3a9 9 0 0 0-9 9c0 3 1.4 5 3 6.5V25h10v-3h3l1-5 2-1-2-4A9 9 0 0 0 14 3z" fill="#2a55a6"/><circle cx="12" cy="11" r="3.2" fill="#fff"/></svg></span>
      <span class="service__label">Testing for<br>Dementia</span>
    </div>

    <div class="service service--left" style="top:235px;">
      <span class="service__icon"><svg width="30" height="30" viewBox="0 0 30 30" fill="none" stroke="#2a55a6" stroke-width="2.4" stroke-linecap="round" stroke-linejoin="round"><path d="M3 12l6-5 5 3 5-3 8 5"/><path d="M8 15l5 5 3-2 3 2 4-4"/></svg></span>
      <span class="service__label">Counseling for<br>Grief &amp; Loss</span>
    </div>
    <div class="service service--right" style="top:235px;">
      <span class="service__icon"><svg width="28" height="28" viewBox="0 0 28 28"><path d="M14 3a9 9 0 0 0-9 9c0 3 1.4 5 3 6.5V25h10v-3h3l1-5 2-1-2-4A9 9 0 0 0 14 3z" fill="#2a55a6"/><circle cx="12" cy="11" r="4" fill="none" stroke="#fff" stroke-width="1.8"/></svg></span>
      <span class="service__label">Behavior<br>Management<br>Interventions</span>
    </div>

    <div class="service service--left" style="top:323px;">
      <span class="service__icon"><svg width="28" height="28" viewBox="0 0 28 28" fill="#2a55a6"><rect x="5" y="6" width="12" height="18"/><rect x="17" y="11" width="7" height="13"/><g fill="#fff"><rect x="7" y="9" width="3" height="2"/><rect x="12" y="9" width="3" height="2"/><rect x="7" y="14" width="3" height="2"/><rect x="12" y="14" width="3" height="2"/><rect x="7" y="19" width="3" height="2"/><rect x="12" y="19" width="3" height="2"/><rect x="19" y="14" width="3" height="2"/><rect x="19" y="19" width="3" height="2"/></g></svg></span>
      <span class="service__label">Help with the<br>Adjustment to<br>a Facility</span>
    </div>
    <div class="service service--right" style="top:323px;">
      <span class="service__icon"><svg width="28" height="28" viewBox="0 0 28 28"><path d="M14 3a9 9 0 0 0-9 9c0 3 1.4 5 3 6.5V25h10v-3h3l1-5 2-1-2-4A9 9 0 0 0 14 3z" fill="#2a55a6"/><path d="M15 6l-3 6h3l-2 6" fill="none" stroke="#fff" stroke-width="1.6"/></svg></span>
      <span class="service__label">Strategies<br>for Managing<br>Pain</span>
    </div>

    <p class="contact">YOU CAN REACH US AT<br>(555) 817-2093</p>
    <div class="web-back">
      <svg width="20" height="20" viewBox="0 0 20 20" fill="none" stroke="#fff" stroke-width="1.4"><circle cx="10" cy="10" r="8.5"/><ellipse cx="10" cy="10" rx="3.8" ry="8.5"/><line x1="1.5" y1="10" x2="18.5" y2="10"/><line x1="3" y1="5.5" x2="17" y2="5.5"/><line x1="3" y1="14.5" x2="17" y2="14.5"/></svg>
      Elmvale.net
    </div>
  </div>

  <div class="landscape" role="img" aria-label="Faded photo of a coastal mountain landscape"></div>
  <svg class="stamp" width="104" height="115" viewBox="0 0 104 115" fill="none" stroke="var(--stamp)" stroke-width="4">
    <path d="M10 6 q6 -6 12 0 q6 6 12 0 q6 -6 12 0 q6 6 12 0 q6 -6 12 0 q6 6 12 0 q6 -6 12 0 q8 2 8 10 q-6 6 0 12 q6 6 0 12 q-6 6 0 12 q6 6 0 12 q-6 6 0 12 q6 6 0 12 q-2 8 -10 8 q-6 -6 -12 0 q-6 6 -12 0 q-6 -6 -12 0 q-6 6 -12 0 q-6 -6 -12 0 q-6 6 -12 0 q-8 -2 -8 -10 q6 -6 0 -12 q-6 -6 0 -12 q6 -6 0 -12 q-6 -6 0 -12 q6 -6 0 -12 q-6 -6 0 -12 q0 -8 6 -8 z"/>
  </svg>
  <div class="address-line address-line--top"></div>
  <div class="address-line address-line--main"></div>
</section>

</body>
</html>
```